Music video company site re-design :-)

Hi guys,

I run a small music video production company called "Copperlane Clip Studio".

It's the new year and I'm hoping to update our website design, but am at a bit of a loss - which is where I'm desperately hoping you can help!

I need something cool and contemporary but not utterly terrifying/confusing that your average band manager/solo artist funding their own music video for the first time, won't be put off.

If you can check out our current website (http://www.CopperlaneClipStudio.example) I think that would probably help :-)

Target Market(s)

Solo music artists and managers of small groups/bands.

Industry/Entity Type

It Company

Requirements
Must have
• Clear, cool but accessible.

I'll need to be able to embed Vimeo videos from our Vimeo-plus account into the pages...

http://www.streamvault.example/copperlaneclips

I'd also like to be able to optimise the site for search engines, so we'll need text and not images with text in them.

I'd also like to include or use images from our videos throughout the site, so if you can include as many of these as possible that would be great.

I've uploaded a zip file with them in, how they are used is up to you guys, but the more the merrier.
Should not have
• Images of cameras, lights, clapper boards etc...

No bloody Times New Roman unless you are really reinventing that wheel or trying to make it look like my nan made my website with clip art.

Also, no god damn emoticons ;-)

```html
<!DOCTYPE html>
<html lang="en">
<head>
<meta charset="utf-8">
<title>Copperlane Clip Studio – Site Pages</title>
<link rel="stylesheet" href="https://fonts.googleapis.com/css2?family=Nunito:wght@800&family=Arimo:wght@400;700&display=swap">
<style>
  :root {
    --bg: #000;
    --text: #e8e8e8;
    --muted: #8a8a8a;
    --magenta: #c53be0;
    --green: #8fd12e;
    --yellow: #e6d41e;
    --cyan: #2fa3e6;
    --logo: #fff;
  }
  * { margin: 0; padding: 0; box-sizing: border-box; }
  html, body { width: 1200px; height: 529px; overflow: hidden; background: var(--bg); }
  body { position: relative; font-family: "Arimo", Arial, sans-serif; color: var(--text); }

  .page { position: absolute; top: 0; width: 300px; height: 529px; overflow: hidden; }
  .page--promo   { left: 0;     --accent: var(--magenta); --glow: 197,59,224; }
  .page--band    { left: 300px; --accent: var(--green);   --glow: 143,209,46; }
  .page--prices  { left: 600px; --accent: var(--yellow);  --glow: 230,212,30; }
  .page--contact { left: 900px; --accent: var(--cyan);    --glow: 40,120,230; }

  .header-art {
    position: absolute; left: 0; top: 0; width: 300px; height: 160px;
    background:
      radial-gradient(ellipse 95px 70px at 200px 45px, rgba(var(--glow),1) 0%, rgba(var(--glow),.55) 45%, rgba(var(--glow),0) 100%),
      radial-gradient(ellipse 60px 45px at 270px 20px, rgba(var(--glow),.8) 0%, rgba(var(--glow),0) 100%),
      radial-gradient(ellipse 70px 40px at 40px 10px, rgba(var(--glow),.45) 0%, rgba(var(--glow),0) 100%),
      radial-gradient(ellipse 120px 60px at 160px 120px, rgba(30,30,30,.9) 0%, rgba(0,0,0,0) 100%);
  }

  .logo {
    position: absolute; left: 31px; top: 40px;
    font-family: "Nunito", Arial, sans-serif; font-weight: 800; color: var(--logo);
    white-space: nowrap; line-height: 1;
  }
  .logo__small { font-size: 9px; margin-right: 3px; }
  .logo__large { font-size: 15px; }

  .nav { position: absolute; left: 18px; top: 81px; width: 62px; list-style: none; text-align: right; }
  .nav li { font-size: 4.6px; font-weight: 700; line-height: 8.2px; color: #fff; letter-spacing: .2px; }
  .nav li.is-active { color: var(--accent); }

  .showreel { position: absolute; left: 177px; top: 78px; font-size: 5.5px; font-weight: 700; color: var(--accent); letter-spacing: .3px; }
  .showreel span { color: #fff; }

  .reel {
    position: absolute; left: 106px; top: 86px; width: 168px; height: 58px;
    background:
      radial-gradient(circle 11px at 55px 22px, rgba(120,200,255,.9), rgba(0,0,0,0)),
      radial-gradient(circle 8px at 110px 26px, rgba(120,200,255,.7), rgba(0,0,0,0)),
      radial-gradient(circle 5px at 140px 15px, rgba(160,220,255,.6), rgba(0,0,0,0)),
      linear-gradient(180deg, #0c1a2c 0%, #06101c 100%);
    border: 1px solid #1c2a3a;
  }

  .content { position: absolute; left: 82px; width: 188px; }
  .content h1 { font-size: 8px; font-weight: 400; color: var(--accent); margin-bottom: 6px; }
  .content p { font-size: 3.6px; line-height: 5px; margin-bottom: 4px; }
  .content .lead { font-weight: 700; color: #fff; }
  .content .fine { color: var(--muted); }
  .content .price-title { font-weight: 700; color: #fff; margin-bottom: 1px; }
  .content .price-title em { font-style: normal; color: var(--accent); }
  .content ul { list-style: none; margin-bottom: 4px; }
  .content li { font-size: 3.6px; line-height: 5px; }
  .contact-entry { margin-bottom: 5px; }
  .contact-entry p { margin-bottom: 0; }

  .still { position: absolute; border-radius: 45% 55% 50% 40%; }
  .page--promo .still   { background: radial-gradient(ellipse at 55% 45%, #f2d6ff 0%, #b640d8 35%, #4a1470 70%, rgba(0,0,0,0) 100%); }
  .page--band .still    { background: radial-gradient(ellipse at 50% 50%, #e8f0c8 0%, #9fc24a 35%, #3b5a16 70%, rgba(0,0,0,0) 100%); }
  .page--prices .still  { background: radial-gradient(ellipse at 45% 50%, #fff6d8 0%, #e8b870 35%, #6e4a18 70%, rgba(0,0,0,0) 100%); }
  .page--contact .still { background: radial-gradient(ellipse at 50% 50%, #d0c8f0 0%, #5a68d0 35%, #1a2466 70%, rgba(0,0,0,0) 100%); }

  .testimonial { position: absolute; left: 106px; width: 160px; }
  .testimonial blockquote { font-size: 3.8px; line-height: 5.2px; font-weight: 700; color: var(--accent); }
  .testimonial cite { display: block; text-align: right; font-style: normal; font-size: 3.4px; color: var(--muted); margin-top: 8px; }
</style>
</head>
<body>

<section class="page page--promo">
  <div class="header-art" role="img" aria-label="Magenta ink splash artwork"></div>
  <div class="logo"><span class="logo__small">COPPERLANE</span><span class="logo__large">CLIP STUDIO</span></div>
  <ul class="nav">
    <li>HOME</li><li>MUSIC VIDEO</li><li class="is-active">PROMO PACKAGE</li><li>BAND SITE DESIGN</li><li>PRICES</li><li>CONTACT US</li>
  </ul>
  <div class="showreel">SHOW<span>REEL</span> 2010</div>
  <div class="reel" role="img" aria-label="Showreel video still with blue stage lights"></div>
  <div class="content" style="top:157px">
    <h1>Promo Package</h1>
    <p class="lead">Great music isn't enough. People need to hear it, and sometimes they need to see it. Seeing a performance will help fans connect with a performer or group in ways that the music alone never could.</p>
    <p>That's why live performances are important and that's also why music videos are important.</p>
    <p>But sometimes, it's not about connecting with fans. Sometimes it's about being recognised as marketable by a record label. An epk with no video is still a very real tool to carry. That's why a Promo Package is important. With a Promo Package we film your single and separate promo material, website, music video, selected tracks, stills and promo shots and a DVD package to help you get noticed.</p>
    <p>Call Osric on 01632 960 101 to chat about what you need or how to start.</p>
    <p>So what are you waiting for? Drop us a line, let's get something made!</p>
  </div>
  <div class="still" style="left:12px;top:254px;width:90px;height:62px" role="img" aria-label="Music video still of a performer in magenta light"></div>
  <div class="testimonial" style="top:295px">
    <blockquote>"I have a great working relationship with CCS and remain continually impressed with their professionalism throughout any of my projects. They have always delivered the goods and within budget. Would definitely work with them again and happily recommend them to anybody..."</blockquote>
    <cite>Marlo Quince, Recording Artist, Lanternfold</cite>
  </div>
</section>

<section class="page page--band">
  <div class="header-art" role="img" aria-label="Green ink splash artwork"></div>
  <div class="logo"><span class="logo__small">COPPERLANE</span><span class="logo__large">CLIP STUDIO</span></div>
  <ul class="nav">
    <li>HOME</li><li>MUSIC VIDEO</li><li>PROMO PACKAGE</li><li class="is-active">BAND SITE DESIGN</li><li>PRICES</li><li>CONTACT US</li>
  </ul>
  <div class="showreel">SHOW<span>REEL</span> 2010</div>
  <div class="reel" role="img" aria-label="Showreel video still with blue stage lights"></div>
  <div class="content" style="top:157px">
    <h1>Band Site Design</h1>
    <p class="lead">One of our main objectives is to support up and coming artists in marketing their music and offer broadcast quality music videos and promos at a fraction of the normal costs, another is to give these artists a platform to promote themselves from.</p>
    <p>That's why we also offer discount website design. As always it's pretty difficult to give an estimate of how much it costs to have a full website made because it depends so much on the design and implementation, however, here's a 'ball park' figure of what you can expect...</p>
    <ul>
      <li>£100 for the first page</li>
      <li>£50 for every page thereafter</li>
      <li>£50 per month maintenance (if needed)</li>
    </ul>
    <p>For a chat about what you need or email: sites@copperlaneclipstudio.example</p>
  </div>
  <div class="still" style="left:12px;top:256px;width:85px;height:60px" role="img" aria-label="Music video still of a band in green light"></div>
  <div class="testimonial" style="top:295px">
    <blockquote>"I have a great working relationship with CCS and remain continually impressed with their professionalism throughout any of my projects. They have always delivered the goods and within budget. Would definitely work with them again and happily recommend them to anybody..."</blockquote>
    <cite>Marlo Quince, Recording Artist, Lanternfold</cite>
  </div>
</section>

<section class="page page--prices">
  <div class="header-art" role="img" aria-label="Yellow ink splash artwork"></div>
  <div class="logo"><span class="logo__small">COPPERLANE</span><span class="logo__large">CLIP STUDIO</span></div>
  <ul class="nav">
    <li>HOME</li><li>MUSIC VIDEO</li><li>PROMO PACKAGE</li><li>BAND SITE DESIGN</li><li class="is-active">PRICES</li><li>CONTACT US</li>
  </ul>
  <div class="showreel">SHOW<span>REEL</span> 2010</div>
  <div class="reel" role="img" aria-label="Showreel video still with blue stage lights"></div>
  <div class="content" style="top:157px">
    <h1>Prices</h1>
    <p class="lead">A cost review to make a good music video. Fact: how much money? That depends on what you want in the video, how many people it needs to make it work and how long it takes to make. Is that a very helpful answer? No, so here are some of those 'ball park' figures we're all so keen on seeing...</p>
    <p class="price-title">Entry Level <em>"January Sale Offer"</em> – £695</p>
    <p>A finished music video for just £695! That's it, no hidden costs, you get a DVD and a web version and you're up and running. Best deal ever!</p>
    <p class="fine">This offer is only available to a signed band or artist with no prior video and expires at the end of January.</p>
    <p class="price-title">Low Budget – up to £1500</p>
    <p>All our productions are shot on full HD and can be rendered to a leading broadcast facilities house, meeting technical broadcast standards. That means videos finished with a 'Low Budget' will be ready to go on TV. Give Osric a call on 01632 960 101 to chat about what you have in mind.</p>
    <p class="price-title">Medium Budget to High Budget – over £1500</p>
    <p>These kinds of budgets are usually from signed clients who want to make a bigger step in promoting themselves, but if you're thinking of having your first video made with us at this kind of budget then call Osric on 01632 960 101.</p>
    <p>...remember that no matter what your budget, we are most interested in making you and your video look as good as possible.</p>
  </div>
  <div class="still" style="left:14px;top:288px;width:84px;height:56px" role="img" aria-label="Music video still of a singer in warm light"></div>
  <div class="testimonial" style="top:325px">
    <blockquote>"I have a great working relationship with CCS and remain continually impressed with their professionalism throughout any of my projects. They have always delivered the goods and within budget. Would definitely work with them again and happily recommend them to anybody..."</blockquote>
    <cite>Marlo Quince, Recording Artist, Lanternfold</cite>
  </div>
</section>

<section class="page page--contact">
  <div class="header-art" role="img" aria-label="Blue ink splash artwork"></div>
  <div class="logo"><span class="logo__small">COPPERLANE</span><span class="logo__large">CLIP STUDIO</span></div>
  <ul class="nav">
    <li>HOME</li><li>MUSIC VIDEO</li><li>PROMO PACKAGE</li><li>BAND SITE DESIGN</li><li>PRICES</li><li class="is-active">CONTACT US</li>
  </ul>
  <div class="showreel">SHOW<span>REEL</span> 2010</div>
  <div class="reel" role="img" aria-label="Showreel video still with blue stage lights"></div>
  <div class="content" style="top:157px">
    <h1>Contact Us</h1>
    <p class="lead">Be brave and give us a call, we definitely won't bite and are always happy to offer help or advice.</p>
    <div class="contact-entry">
      <p>Wren Halloway</p><p>Producer / Director, Location Manager</p><p>wren@copperlaneclipstudio.example</p><p class="fine">01632 960 100 or 01632 960 200</p>
    </div>
    <div class="contact-entry">
      <p>Osric Tamblyn</p><p>Director / Producer</p><p>osric@copperlaneclipstudio.example</p><p class="fine">01632 960 101 or 01632 960 201</p>
    </div>
    <div class="contact-entry">
      <p>Juno Faircloth</p><p>Production Co-ordinator / Account Dept.</p><p>juno@copperlaneclipstudio.example</p>
    </div>
    <div class="contact-entry">
      <p>Perpetua Lyle</p><p>Producer / Talent Management</p><p>perpetua@copperlaneclipstudio.example</p>
    </div>
    <div class="contact-entry">
      <p>Anselm Rook</p><p>Editor / Production Assistant</p><p>anselm@copperlaneclipstudio.example</p>
    </div>
  </div>
  <div class="still" style="left:12px;top:290px;width:88px;height:56px" role="img" aria-label="Music video still of a performer in blue light"></div>
  <div class="testimonial" style="top:328px">
    <blockquote>"I have a great working relationship with CCS and remain continually impressed with their professionalism throughout any of my projects. They have always delivered the goods and within budget. Would definitely work with them again and happily recommend them to anybody..."</blockquote>
    <cite>Marlo Quince, Recording Artist, Lanternfold</cite>
  </div>
</section>

</body>
</html>
```